Career Counselor in need of a business card design

Hello Creatives! I'm in need of a business card design for a new company based in Georgia, USA called Pathways By Lumen.

Some things that may be helpful in creating your concept(s) include:

My Logo (Included in the Files section): There are three versions, two versions are in the second file. The all gold stacked (vertical) version is my primary logo and then there are two horizontal versions (one is all gold and the other is gold and grey).

My mission: to empower tweens through young adults to realize and actualize their CAREER ASPIRATIONS.
My vision: for tweens through young adults to LIVE LIFE ON PURPOSE and become CONTRIBUTING MEMBERS OF SOCIETY.

Biblical scriptures that support my ‘Why’: Psalms 127: 3-4(NIV) Children are a heritage from the Lord, offspring a reward from him. Like ARROWS in the hands of a warrior are children…. And Proverbs 29:18(JKV) Where there is no VISION, the people perish.

*Words in ALL CAPS are to emphasize what's important to me and may possibly provide you some inspiration (IDK - Have fun with it)!

Target Market(s)

My ideal customers are parents, guardians, and young adults.

Contact Information for Business Card

My name, degrees and credential: Delmira Fosket, M.A., Ed.D., LPC
Title: Academic and Career Coach and Consultant

Number: 555.317.8842
Address: 2618 Velbrook Avenue., Suite 407, Carrowfield, TN 38412
Email: info@pathwaysbylumen.co
Website: www.pathwaysbylumen.co

My population: TWEENS • TEENS • EMERGING ADULTS
Services offered: One-On-One Sessions • Small Groups • Workshops

Colors

Designer to choose colors to be used in the design.

Requirements
Nice to have
• Either my mission or vision but I will understand if it does not all fit.
• My mission: To empower tweens through young adults to realize and actualize their career aspirations.
• My vision: For tweens through young adults to live life on purpose and become contributing members of society.

```html
<!DOCTYPE html>
<html lang="en">
<head>
<meta charset="utf-8">
<title>Pathways By Lumen — Business Card Design</title>
<link href="https://fonts.googleapis.com/css2?family=Cinzel:wght@400;600&family=Arimo:wght@400&display=swap" rel="stylesheet">
<style>
:root{
  --page:#ebe7e1;
  --label:#6b5d4c;
  --gold:#c9a23c;
  --gold-band:linear-gradient(90deg,#c59a35 0%,#f5de8c 40%,#d8b452 70%,#b98f2c 100%);
  --gold-panel:linear-gradient(180deg,#d3ad50 0%,#c59c3c 100%);
  --cream:linear-gradient(90deg,#f6ecd2 0%,#eadbb4 100%);
  --ink:#1c1c1c;
  --black:#050505;
  --white:#ffffff;
  --panel-ink:#2a2418;
  --panel-light:#fdf3d6;
}
*{margin:0;padding:0;box-sizing:border-box}
html,body{width:1200px;height:1200px;overflow:hidden;background:var(--page)}
.sheet{position:relative;width:1200px;height:1200px}
.sheet-label{position:absolute;left:55px;font-family:"Arimo",Arial,sans-serif;font-size:21px;color:var(--label)}
.card{position:absolute;width:406px;height:242px;overflow:hidden;box-shadow:0 2px 6px rgba(0,0,0,.25);font-family:"Cinzel",serif}
.col-front{left:159px}
.col-back{left:637px}

/* front v1 */
.front-light{background:var(--white)}
.front-light .band{position:absolute;left:0;width:100%;background:var(--gold-band)}
.front-light .band-top{top:0;height:48px}
.front-light .band-bottom{bottom:0;height:50px;display:flex;align-items:center;justify-content:center}
.faint-circle{position:absolute;border-radius:50%;border:34px solid rgba(220,196,130,.22)}
.front-light .faint-circle{left:75px;top:-10px;width:260px;height:260px}
.services{font-size:11.5px;letter-spacing:.3px;white-space:nowrap}
.front-light .services{color:#fff6da;text-shadow:0 0 1px rgba(120,90,20,.5)}

.brand{position:absolute;left:72px;top:84px;display:flex;align-items:center;gap:14px}
.brand-dot{width:74px;height:74px;border-radius:50%;border:4px solid var(--gold)}
.brand-name{font-weight:600;font-size:27px;line-height:1.05;color:var(--gold);padding-left:12px;border-left:2px solid var(--gold)}

/* front v2 */
.front-dark{background:var(--black)}
.front-dark .frame{position:absolute;left:26px;top:26px;right:26px;bottom:29px;border:1px solid var(--gold)}
.front-dark .frame-foot{position:absolute;left:0;right:0;bottom:-7px;display:flex;justify-content:center}
.front-dark .frame-foot .services{background:var(--black);padding:0 8px;color:var(--gold);font-size:12px}

/* backs */
.back{background:var(--white);color:var(--ink)}
.back .panel{position:absolute;top:0;right:0;height:100%}
.back-v1 .panel{width:151px;background:var(--cream)}
.back-v2 .panel{width:137px;background:var(--gold-panel)}
.back .faint-circle{left:190px;top:30px;width:180px;height:180px;border-width:24px;border-color:rgba(214,182,100,.25)}
.person{position:absolute;left:28px;top:22px;z-index:1}
.person-name{font-size:14px;font-weight:400;line-height:1}
.person-creds{font-size:9px;line-height:1.2}
.person-title{font-size:11px;line-height:1.2;margin-top:12px}
.back-v2 .person-title{margin-top:10px}
.contact{position:absolute;left:28px;font-size:9.5px;line-height:1.2;list-style:none;z-index:1}
.back-v1 .contact{top:138px}
.back-v1 .contact li{margin-bottom:6px}
.back-v2 .contact{top:127px}
.back-v2 .contact li{display:flex;gap:6px;margin-bottom:5px;align-items:flex-start}
.icon{flex:none;width:11px;height:11px;margin-top:1px}
.statement{position:absolute;right:27px;top:24px;text-align:right;list-style:none;font-size:10px}
.back-v1 .statement,.back-v1 .population{color:var(--panel-ink)}
.back-v2 .statement,.back-v2 .population{color:var(--panel-light)}
.mission li{margin-bottom:9px}
.back-v2 .mission li{margin-bottom:12.3px}
.vision li{line-height:15px}
.population{position:absolute;right:27px;bottom:24px;text-align:right;font-size:11px;line-height:11px}
</style>
</head>
<body>
<main class="sheet">

  <p class="sheet-label" style="top:26px">Business Card Design - version 1 &amp; 2 with Mission words</p>
  <p class="sheet-label" style="top:611px">Business Card Design - version 1 &amp; 2 with Vision words</p>

  <!-- Row 1: light front + mission back -->
  <section class="card front-light col-front" style="top:63px">
    <div class="band band-top"></div>
    <div class="faint-circle"></div>
    <div class="brand"><span class="brand-dot"></span><span class="brand-name">Pathways<br>By Lumen</span></div>
    <div class="band band-bottom"><span class="services">One-On-One Sessions · Small Groups · Workshops</span></div>
  </section>

  <section class="card back back-v1 col-back" style="top:63px">
    <div class="panel"></div>
    <div class="faint-circle"></div>
    <div class="person">
      <p class="person-name">Delmira Fosket</p>
      <p class="person-creds">M.A., Ed.D., LPC</p>
      <p class="person-title">Academic and Career<br>Coach and Consultant</p>
    </div>
    <ul class="contact">
      <li>555.317.8842</li>
      <li>2618 Velbrook Avenue,<br>Suite 407, Carrowfield, TN 38412</li>
      <li>info@pathwaysbylumen.co</li>
      <li>www.pathwaysbylumen.co</li>
    </ul>
    <ul class="statement mission">
      <li>My Mission:</li><li>To empower</li><li>tweens</li><li>through</li><li>young adults</li><li>to realize</li><li>and actualize</li><li>their career</li><li>aspirations</li>
    </ul>
  </section>

  <!-- Row 2: dark front + mission back -->
  <section class="card front-dark col-front" style="top:337px">
    <div class="frame"><div class="frame-foot"><span class="services">One-On-One Sessions · Small Groups · Workshops</span></div></div>
    <div class="brand"><span class="brand-dot"></span><span class="brand-name">Pathways<br>By Lumen</span></div>
  </section>

  <section class="card back back-v2 col-back" style="top:337px">
    <div class="panel"></div>
    <div class="faint-circle"></div>
    <div class="person">
      <p class="person-name">Delmira Fosket</p>
      <p class="person-creds">M.A., Ed.D., LPC</p>
      <p class="person-title">Academic &amp;<br>Career<br>Coach &amp; Consultant</p>
    </div>
    <ul class="contact">
      <li><svg class="icon" viewBox="0 0 12 12"><circle cx="6" cy="6" r="6" fill="#c9a23c"/><path d="M4 3l1.3 0 .5 1.6-.8.6a4 4 0 0 0 1.8 1.8l.6-.8 1.6.5V8A1 1 0 0 1 8 9 5 5 0 0 1 3 4a1 1 0 0 1 1-1z" fill="#fff"/></svg>555.317.8842</li>
      <li><svg class="icon" viewBox="0 0 12 12"><circle cx="6" cy="6" r="6" fill="#c9a23c"/><path d="M6 2.5a2.3 2.3 0 0 1 2.3 2.3C8.3 6.5 6 9.5 6 9.5S3.7 6.5 3.7 4.8A2.3 2.3 0 0 1 6 2.5z" fill="#fff"/><circle cx="6" cy="4.8" r=".9" fill="#c9a23c"/></svg>2618 Velbrook<br>Avenue., Suite 407,<br>Carrowfield, TN 38412</li>
      <li><svg class="icon" viewBox="0 0 12 12"><circle cx="6" cy="6" r="6" fill="#c9a23c"/><rect x="3" y="4" width="6" height="4.2" fill="#fff"/><path d="M3 4l3 2.3L9 4" stroke="#c9a23c" stroke-width=".7" fill="none"/></svg>info@pathwaysbylumen.co</li>
      <li><svg class="icon" viewBox="0 0 12 12"><circle cx="6" cy="6" r="6" fill="#c9a23c"/><rect x="3" y="3.3" width="6" height="5" rx=".5" fill="#fff"/><rect x="3" y="3.3" width="6" height="1.2" fill="#8c6d22"/></svg>www.pathwaysbylumen.co</li>
    </ul>
    <ul class="statement mission">
      <li>My Mission:</li><li>To empower</li><li>tweens through</li><li>young adults</li><li>to realize</li><li>and actualize</li><li>their career</li><li>aspirations</li>
    </ul>
  </section>

  <!-- Row 3: light front + vision back -->
  <section class="card front-light col-front" style="top:655px">
    <div class="band band-top"></div>
    <div class="faint-circle"></div>
    <div class="brand"><span class="brand-dot"></span><span class="brand-name">Pathways<br>By Lumen</span></div>
    <div class="band band-bottom"><span class="services">One-On-One Sessions · Small Groups · Workshops</span></div>
  </section>

  <section class="card back back-v1 col-back" style="top:655px">
    <div class="panel"></div>
    <div class="faint-circle"></div>
    <div class="person">
      <p class="person-name">Delmira Fosket</p>
      <p class="person-creds">M.A., Ed.D., LPC</p>
      <p class="person-title">Academic and Career<br>Coach and Consultant</p>
    </div>
    <ul class="contact">
      <li>555.317.8842</li>
      <li>2618 Velbrook Avenue,<br>Suite 407, Carrowfield, TN 38412</li>
      <li>info@pathwaysbylumen.co</li>
      <li>www.pathwaysbylumen.co</li>
    </ul>
    <ul class="statement vision">
      <li>My Vision:</li><li>For tweens</li><li>through</li><li>young adults</li><li>to live life</li><li>on purpose</li><li>and become</li><li>contributing</li><li>members of</li><li>society.</li>
    </ul>
    <p class="population">Tweens, Teens,<br>Emerging Adults</p>
  </section>

  <!-- Row 4: dark front + vision back -->
  <section class="card front-dark col-front" style="top:929px">
    <div class="frame"><div class="frame-foot"><span class="services">One-On-One Sessions · Small Groups · Workshops</span></div></div>
    <div class="brand"><span class="brand-dot"></span><span class="brand-name">Pathways<br>By Lumen</span></div>
  </section>

  <section class="card back back-v2 col-back" style="top:929px">
    <div class="panel"></div>
    <div class="faint-circle"></div>
    <div class="person">
      <p class="person-name">Delmira Fosket</p>
      <p class="person-creds">M.A., Ed.D., LPC</p>
      <p class="person-title">Academic &amp;<br>Career<br>Coach &amp; Consultant</p>
    </div>
    <ul class="contact">
      <li><svg class="icon" viewBox="0 0 12 12"><circle cx="6" cy="6" r="6" fill="#c9a23c"/><path d="M4 3l1.3 0 .5 1.6-.8.6a4 4 0 0 0 1.8 1.8l.6-.8 1.6.5V8A1 1 0 0 1 8 9 5 5 0 0 1 3 4a1 1 0 0 1 1-1z" fill="#fff"/></svg>555.317.8842</li>
      <li><svg class="icon" viewBox="0 0 12 12"><circle cx="6" cy="6" r="6" fill="#c9a23c"/><path d="M6 2.5a2.3 2.3 0 0 1 2.3 2.3C8.3 6.5 6 9.5 6 9.5S3.7 6.5 3.7 4.8A2.3 2.3 0 0 1 6 2.5z" fill="#fff"/><circle cx="6" cy="4.8" r=".9" fill="#c9a23c"/></svg>2618 Velbrook<br>Avenue., Suite 407,<br>Carrowfield, TN 38412</li>
      <li><svg class="icon" viewBox="0 0 12 12"><circle cx="6" cy="6" r="6" fill="#c9a23c"/><rect x="3" y="4" width="6" height="4.2" fill="#fff"/><path d="M3 4l3 2.3L9 4" stroke="#c9a23c" stroke-width=".7" fill="none"/></svg>info@pathwaysbylumen.co</li>
      <li><svg class="icon" viewBox="0 0 12 12"><circle cx="6" cy="6" r="6" fill="#c9a23c"/><rect x="3" y="3.3" width="6" height="5" rx=".5" fill="#fff"/><rect x="3" y="3.3" width="6" height="1.2" fill="#8c6d22"/></svg>www.pathwaysbylumen.co</li>
    </ul>
    <ul class="statement vision">
      <li>My Vision:</li><li>For tweens</li><li>through</li><li>young adults</li><li>to live life</li><li>on purpose</li><li>and become</li><li>contributing</li><li>members of</li><li>society.</li>
    </ul>
    <p class="population">Tweens, Teens,<br>Emerging Adults</p>
  </section>

</main>
</body>
</html>
```